Crestline Strength Mural

Need the design for a large sign writing mural to go on this Powerlifting gym wall (photo) 3meters high x 9 meters long. Note a bite of 90cm high and 60cm deep is taken out at one end by the low cupboard you see. Logo files are attached -- the image would be some elaboration, stretching, repletion, whatever of the logo. The two Squat racks you see in the photo will stay permanently and be used there. Wall is being painted basic white tomorrow. Job is in Preston, Melbourne, Australia. I will arrange a signwriter when the design is worked out. Design and appropriately sized artwork file needed in c 3 days max.

```html
<!DOCTYPE html>
<html lang="en">
<head>
<meta charset="utf-8">
<title>Crestline Strength Mural</title>
<link href="https://fonts.googleapis.com/css2?family=Archivo+Black&display=swap" rel="stylesheet">
<style>
  :root {
    --ink: #0b0b0b;
    --signal-red: #c8302f;
    --wall-white: #ffffff;
    --backdrop: #eceae6;
  }
  * { box-sizing: border-box; margin: 0; padding: 0; }
  html, body {
    width: 900px;
    height: 1200px;
    overflow: hidden;
    background: var(--backdrop);
  }
  .canvas {
    position: relative;
    width: 900px;
    height: 1200px;
    display: flex;
    align-items: center;
    justify-content: center;
  }
  .mural {
    position: relative;
    width: 840px;
    height: 280px;
    background: var(--wall-white);
    overflow: hidden;
  }
  .edge-band {
    position: absolute;
    left: 0;
    width: 100%;
    height: 24px;
    background: linear-gradient(90deg, var(--ink), var(--signal-red));
  }
  .edge-band--top { top: 0; }
  .edge-band--bottom { bottom: 0; }
  .brand-lockup {
    position: absolute;
    top: 24px;
    bottom: 24px;
    left: 0;
    right: 0;
    display: flex;
    align-items: center;
    justify-content: center;
    gap: 30px;
    padding-right: 20px;
  }
  .brand-mark {
    width: 104px;
    height: 104px;
    border-radius: 50%;
    background: var(--signal-red);
    flex: none;
  }
  .brand-name {
    font-family: "Archivo Black", "Arial Black", sans-serif;
    font-weight: 400;
    color: var(--ink);
    text-transform: uppercase;
    line-height: 0.92;
    letter-spacing: -1px;
  }
  .brand-name .line-main { display: block; font-size: 86px; }
  .brand-name .line-sub { display: block; font-size: 62px; margin-top: 6px; }
</style>
</head>
<body>
  <main class="canvas">
    <section class="mural">
      <div class="edge-band edge-band--top" role="img" aria-label="Decorative red and black border band"></div>
      <div class="brand-lockup">
        <span class="brand-mark" aria-hidden="true"></span>
        <h1 class="brand-name">
          <span class="line-main">Crestline</span>
          <span class="line-sub">Strength</span>
        </h1>
      </div>
      <div class="edge-band edge-band--bottom" role="img" aria-label="Decorative red and black border band"></div>
    </section>
  </main>
</body>
</html>
```